Business cards for Harbourline Supply Pty Ltd that import building products into Australia from China
Target Market(s)
Business to Business
Industry/Entity Type
Business
Contact Information for Business Card
Front: Logo and Business Name
Rear:
Vernon Ashcombe
General Manager
Mobile: 0427 619 354
email: vern@harbourlinesupply.com.au
alternative email: vern@coastwardgoods.com.au
web: www.harbourlinesupply.com.au
Perth, Hobart and Cairns
Colors
ec1f27
fbee3d

```html
<!DOCTYPE html>
<html lang="en">
<head>
<meta charset="utf-8">
<title>Harbourline Supply Pty Ltd – Business Cards</title>
<link rel="stylesheet" href="https://fonts.googleapis.com/css2?family=Roboto:wght@700&family=Roboto+Condensed:wght@400;700&display=swap">
<style>
  :root {
    --red: #ec1f27;
    --yellow: #fbee3d;
    --yellow-light: #f8ef86;
    --ink: #111111;
    --grey: #6d6a63;
    --backdrop: #1c1c1e;
  }
  * { box-sizing: border-box; margin: 0; padding: 0; }
  html, body { width: 1200px; height: 900px; overflow: hidden; }
  body {
    background: var(--backdrop);
    position: relative;
    font-family: "Roboto Condensed", "Arial Narrow", sans-serif;
  }
  .card {
    position: absolute;
    width: 540px;
    height: 328px;
    overflow: hidden;
    box-shadow: 0 12px 30px rgba(0,0,0,.45);
  }
  .card--front {
    left: 620px; top: 140px;
    background: var(--yellow);
  }
  .brand {
    position: absolute;
    left: 0; right: 0; top: 78px;
    display: flex; flex-direction: column; align-items: center;
  }
  .brand__mark {
    width: 118px; height: 96px;
    background: var(--red);
    display: flex; align-items: center; justify-content: center;
    font-family: "Roboto", Arial, sans-serif;
    font-weight: 700; font-size: 24px; line-height: 1.05;
    color: var(--ink); text-align: center;
  }
  .brand__name {
    margin-top: 8px;
    font-family: "Roboto", Arial, sans-serif;
    font-weight: 700; font-size: 25px;
    color: var(--ink);
    white-space: nowrap;
  }
  .card--back {
    left: 40px; top: 480px;
    background: var(--red);
  }
  .person {
    position: absolute; left: 30px; top: 26px;
    color: var(--grey);
  }
  .person__name {
    font-weight: 700; font-size: 27px; text-transform: uppercase;
    letter-spacing: 0.3px;
  }
  .person__role { font-size: 18px; margin-top: 2px; }
  .ribbons { position: absolute; left: 0; top: 0; width: 540px; height: 328px; }
  .contacts {
    position: absolute; right: 26px; top: 148px;
    list-style: none;
    color: var(--grey);
  }
  .contacts li {
    height: 42px;
    display: flex; align-items: center; justify-content: flex-end; gap: 10px;
    font-size: 15px;
    white-space: nowrap;
  }
  .contacts .contacts__phone { font-size: 20px; }
  .contacts .stack { display: flex; flex-direction: column; align-items: flex-end; line-height: 1.15; font-size: 13px; }
  .icon { width: 26px; height: 26px; flex: none; }
</style>
</head>
<body>

<section class="card card--front" aria-label="Business card front">
  <div class="brand">
    <div class="brand__mark">Logo<br>Here</div>
    <div class="brand__name">Harbourline Supply Pty Ltd</div>
  </div>
</section>

<section class="card card--back" aria-label="Business card back">
  <svg class="ribbons" viewBox="0 0 540 328" aria-hidden="true">
    <polygon points="150,148 540,148 540,186 150,186 170,167" fill="var(--yellow)"/>
    <polygon points="150,148 540,148 540,156 158,156" fill="var(--yellow-light)"/>
    <polygon points="110,190 540,190 540,228 110,228 130,209" fill="var(--yellow)"/>
    <polygon points="110,190 540,190 540,198 118,198" fill="var(--yellow-light)"/>
    <polygon points="70,232 540,232 540,270 70,270 90,251" fill="var(--yellow)"/>
    <polygon points="70,232 540,232 540,240 78,240" fill="var(--yellow-light)"/>
    <polygon points="30,274 540,274 540,312 30,312 50,293" fill="var(--yellow)"/>
    <polygon points="30,274 540,274 540,282 38,282" fill="var(--yellow-light)"/>
  </svg>

  <div class="person">
    <div class="person__name">Vernon Ashcombe</div>
    <div class="person__role">General Manager</div>
  </div>

  <ul class="contacts">
    <li class="contacts__phone">0427 619 354
      <svg class="icon" viewBox="0 0 28 28" aria-label="Phone"><circle cx="14" cy="14" r="13" fill="var(--red)"/><path d="M9 8c1-1 2-1 2.6 0l1.4 2.4c.4.7.2 1.3-.4 1.8l-.8.6c.8 1.7 2 2.9 3.6 3.7l.6-.8c.5-.6 1.1-.8 1.8-.4l2.4 1.4c1 .6 1 1.6 0 2.6-1 1-2.6 1.6-4.6.5-3-1.6-5.5-4.2-7-7.2-.9-2-.6-3.5.4-4.6z" fill="var(--yellow)"/></svg>
    </li>
    <li>
      <span class="stack"><span>vern@harbourlinesupply.com.au</span><span>vern@coastwardgoods.com.au</span></span>
      <svg class="icon" viewBox="0 0 28 28" aria-label="Email"><circle cx="14" cy="14" r="13" fill="var(--red)"/><rect x="7" y="9" width="14" height="10" rx="1" fill="var(--yellow)"/><path d="M7.5 9.5 14 15l6.5-5.5" fill="none" stroke="var(--red)" stroke-width="1.4"/></svg>
    </li>
    <li>www.harbourlinesupply.com.au
      <svg class="icon" viewBox="0 0 28 28" aria-label="Website"><circle cx="14" cy="14" r="13" fill="var(--red)"/><circle cx="14" cy="14" r="7" fill="none" stroke="var(--yellow)" stroke-width="1.6"/><ellipse cx="14" cy="14" rx="3" ry="7" fill="none" stroke="var(--yellow)" stroke-width="1.4"/><path d="M7 14h14" stroke="var(--yellow)" stroke-width="1.4"/></svg>
    </li>
    <li>Perth, Hobart and Cairns
      <svg class="icon" viewBox="0 0 28 28" aria-label="Location"><circle cx="14" cy="14" r="13" fill="var(--red)"/><path d="M14 6a5 5 0 0 1 5 5c0 3.6-5 10-5 10s-5-6.4-5-10a5 5 0 0 1 5-5z" fill="var(--yellow)"/><circle cx="14" cy="11" r="2" fill="var(--red)"/></svg>
    </li>
  </ul>
</section>

</body>
</html>
```